Construction Company Website Design

I need a Website Design for a Construction Company. I have attached logo and business card design files (a.i) to match styles and text for the website. I will need design for 3 pages:
1. A Home page
2. A secondary page (will be different information pages)
3. A contact page with submision form
Website to look professional and match the 'theme' across all pages, using main colours / reverse colours as per design files. Must be clear it is a construction related website without being over the top. Happy for the construction related details (whether that be images/outlines/backgrounds etc to be fairly subtle and not overbearing on the contect of the pages. It will be the content that will be most important, not the images within.

Content has not yet been fully completed but attached is a site map. Each page will need a space for the insertion of the relevant heading and associated content for that particular page. Example can be used as per attached map. If it is preferable to have content completed for this to be a more succesful project please advise and I will complete and submit.

Target Market(s)

Clients for potential construction projects. These could be a range of people. All would be very professional, well educated and put a substantial expection on the quality of website provided.

Industry/Entity Type

Construction

Number of Pages Required

3 page

Font styles to use
Serif
Sans Serif
Other font styles liked:
• fonts preferable as per design files provided unless designer beleives a different font would suit better

Requirements
Must have
• Colour scheme to match logo and business card files provided. Fonts that match as per provided files. Pages must be consistent with the theme carrying across all pages. All pages must have contact details at the bottom of the page.
• Contents of page 1 - 'Home page': multiple tab options / logo link
• Contents of page 2 - 'Secondary page': Top and side navigation / area for information and/or images.
• Contents of page - 'Contact us page': Top and side navigation / Submission form / area for logos such as linkdin, facebook etc.
Nice to have
• Would be good to have a or some generic construction related images - outlines / shadows / effects etc. These might be background images or outlines related to the relevant industry and are consistent across the pages. Could be outlines of buildings, images of men with hardhats etc etc. Good to see colour scheme as per design files used
Should not have
• No pictures of houses. Generally no photos. If any imagery of people must not show faces/details.

```html
<!DOCTYPE html>
<html lang="en">
<head>
<meta charset="utf-8">
<title>KVR Constructions</title>
<link href="https://fonts.googleapis.com/css2?family=Michroma&family=Arimo:wght@400;700&display=swap" rel="stylesheet">
<style>
:root{
  --blue:#1e88d8;
  --blue-light:#2fa6ea;
  --ink:#3a3a3a;
  --text:#6b6b6b;
  --grey-bg:#f4f4f4;
  --line:#dcdcdc;
  --dark:#1f1f1f;
  --white:#ffffff;
}
*{box-sizing:border-box;margin:0;padding:0}
html,body{width:1200px;height:2995px;overflow:hidden}
body{position:relative;background:var(--white);font-family:"Arimo",Arial,sans-serif;color:var(--text)}
.abs{position:absolute}

/* header */
.site-header{left:0;top:0;width:1200px;height:92px;background:var(--white)}
.brand{left:84px;top:32px;display:flex;align-items:center;gap:10px;font-family:"Arimo",Arial,sans-serif;font-weight:400;font-size:24px;color:#444;white-space:nowrap}
.brand .dot{width:14px;height:14px;background:var(--blue)}
.call{left:868px;top:18px;display:flex;align-items:center;gap:10px;font-family:"Michroma",sans-serif;font-size:12px;color:var(--blue);white-space:nowrap}
.call .icon{width:50px;height:50px;border-radius:50%;background:var(--blue);display:flex;align-items:center;justify-content:center}

.main-nav{left:0;top:92px;width:1200px;height:58px;background:var(--blue)}
.main-nav a{position:absolute;top:22px;font-family:"Michroma",sans-serif;font-size:10px;color:var(--white);text-decoration:none;letter-spacing:.5px}
.main-nav .sep{position:absolute;top:24px;width:1px;height:10px;background:rgba(255,255,255,.6)}

/* hero */
.hero{left:0;top:150px;width:1200px;height:544px;overflow:hidden}
.hero-art{left:0;top:0;width:1200px;height:544px;background:linear-gradient(90deg,#d9d9d9 0%,#f3f3f3 40%,#e7e7e7 60%)}
.hero-panel{left:0;top:0}
.hero-title{left:684px;top:262px;font-family:"Michroma",sans-serif;font-size:24px;color:var(--white);letter-spacing:2px;white-space:nowrap}
.hero-copy{left:684px;top:316px;width:460px;font-size:12px;line-height:26px;color:var(--white)}
.btn-hero{left:682px;top:414px;width:234px;height:48px;border-radius:24px;background:var(--blue);color:var(--white);font-family:"Michroma",sans-serif;font-size:10px;display:flex;align-items:center;justify-content:center}
.dots{left:1062px;top:526px;display:flex;gap:4px}
.dots span{width:10px;height:10px;border-radius:50%;background:#333}
.dots span.on{background:var(--white)}

/* section headings */
.section-title{width:1200px;left:0;text-align:center;font-family:"Michroma",sans-serif;font-size:24px;font-weight:400;color:var(--ink);letter-spacing:1px}
.rule{left:564px;width:74px;height:3px;background:var(--blue)}
.section-sub{width:1200px;left:0;text-align:center;font-size:12px;color:var(--text)}

/* services */
.services{left:0;top:694px;width:1200px;height:524px;background:var(--grey-bg)}
.service-card{top:190px;width:244px;height:278px;background:var(--white);border:1px solid var(--line);border-radius:3px;text-align:center}
.service-card.active{box-shadow:0 4px 12px rgba(0,0,0,.18);border-bottom:5px solid var(--blue)}
.service-card svg{margin-top:34px}
.service-card h3{margin-top:16px;font-family:"Michroma",sans-serif;font-size:11px;color:var(--blue);font-weight:400;white-space:nowrap}
.service-card p{margin:22px auto 0;width:214px;font-size:11px;line-height:24px}

/* about */
.about-img{left:126px;top:1270px;width:504px;height:370px;background:linear-gradient(135deg,#9cc6ea,#2f6db0 60%,#d7e8f6)}
.about-box{left:554px;top:1410px;width:522px;height:290px;background:var(--white);border:1px solid var(--line);box-shadow:0 2px 10px rgba(0,0,0,.08);overflow:hidden}
.about-box h2{position:absolute;left:38px;top:42px;font-family:"Michroma",sans-serif;font-size:22px;color:var(--ink);font-weight:400}
.about-box .rule{position:absolute;left:38px;top:84px}
.about-box p{position:absolute;left:40px;top:106px;width:442px;font-size:11.5px;line-height:27px}
.corner{position:absolute;right:0;bottom:0}

/* testimonials */
.testimonials{left:0;top:1750px;width:1200px;height:390px;background:linear-gradient(180deg,#1aa2e8,#1e8bd9 70%,#3aa8ea)}
.quote{left:230px;top:172px;width:740px;text-align:center;font-size:11.5px;line-height:27px;color:#dff1fd}
.author{left:0;width:1200px;text-align:center;top:280px;font-family:"Michroma",sans-serif;font-size:12px;color:var(--white)}
.posted{left:0;width:1200px;text-align:center;top:304px;font-size:12px;color:var(--white)}

/* projects */
.projects{left:0;top:2140px;width:1200px;height:594px;background:linear-gradient(180deg,#f7f7f7,#ffffff)}
.project-card{top:134px;width:318px;height:410px;background:var(--white);border:1px solid var(--line);text-align:center}
.project-card.active{box-shadow:0 3px 12px rgba(0,0,0,.2)}
.project-card .thumb{height:204px}
.project-card h3{margin-top:22px;font-family:"Michroma",sans-serif;font-size:14px;color:var(--ink);font-weight:400}
.project-card p{margin:14px auto 0;width:270px;font-size:11.5px;line-height:26px}
.btn-more{display:inline-flex;margin-top:16px;width:112px;height:34px;border-radius:17px;background:var(--blue);color:var(--white);align-items:center;justify-content:center;font-family:"Michroma",sans-serif;font-size:10px}

/* footer */
.site-footer{left:0;top:2734px;width:1200px;height:261px;background:var(--dark);color:var(--white)}
.footer-brand{left:128px;top:86px;display:flex;align-items:center;gap:10px;font-family:"Arimo",Arial,sans-serif;font-weight:400;font-size:22px;color:var(--white);white-space:nowrap}
.footer-brand .dot{width:12px;height:12px;background:var(--blue)}
.footer-head{font-family:"Arimo",Arial,sans-serif;font-weight:700;font-size:14px;letter-spacing:.5px;top:28px}
.footer-links a{position:absolute;font-size:12px;color:var(--white);text-decoration:none}
.news-text{left:764px;top:72px;font-size:12px}
.email{left:764px;top:106px;width:294px;height:48px;background:var(--white);color:#555;font-size:12px;padding:17px 20px}
.email-btn{left:1056px;top:106px;width:46px;height:48px;background:var(--blue);display:flex;align-items:center;justify-content:center}
.footer-rule{left:84px;top:198px;width:1032px;height:1px;background:#333}
.copyright{left:0;top:224px;width:1200px;text-align:center;font-size:12px}
</style>
</head>
<body>

<header class="site-header abs">
  <div class="brand abs"><span class="dot"></span>KVR Constructions</div>
  <div class="call abs">
    <span class="icon"><svg width="20" height="20" viewBox="0 0 24 24"><path fill="#fff" d="M6.6 10.8a15.1 15.1 0 0 0 6.6 6.6l2.2-2.2c.3-.3.7-.4 1-.2 1.1.4 2.3.6 3.6.6.6 0 1 .4 1 1V20c0 .6-.4 1-1 1A17 17 0 0 1 3 4c0-.6.4-1 1-1h3.5c.6 0 1 .4 1 1 0 1.3.2 2.5.6 3.6.1.3 0 .7-.2 1z"/></svg></span>
    CALL US : 0400 123 987
  </div>
</header>

<nav class="main-nav abs">
  <a style="left:140px">HOME</a><span class="sep" style="left:222px"></span>
  <a style="left:260px">ABOUT US</a><span class="sep" style="left:372px"></span>
  <a style="left:412px">SERVICES</a><span class="sep" style="left:526px"></span>
  <a style="left:564px">PROJECTS</a><span class="sep" style="left:680px"></span>
  <a style="left:720px">CULTURE</a><span class="sep" style="left:834px"></span>
  <a style="left:868px">NEWS</a><span class="sep" style="left:952px"></span>
  <a style="left:988px">CONTACT</a>
</nav>

<section class="hero abs">
  <div class="hero-art abs" role="img" aria-label="Line drawing of city skyscrapers in grey and blue"></div>
  <svg class="hero-panel abs" width="1200" height="544">
    <polygon points="786,0 800,0 546,544 530,544" fill="#8a8a8a"/>
    <polygon points="800,0 1200,0 1200,544 546,544" fill="#2a9ce6" opacity=".92"/>
  </svg>
  <h1 class="hero-title abs" style="font-weight:400">KVR CONSTRUCTIONS</h1>
  <p class="hero-copy abs">Sed ut perspiciatis unde omnis iste natus error sit voluptatem accusantium dolorem que laudantium, totam rem aperiam, eaque ipsa quae ab illo inventore veritatis et quasi architecto beatae vitae dicta sunt explicabo.</p>
  <div class="btn-hero abs">CLICK HERE FOR MORE INFO</div>
  <div class="dots abs"><span></span><span class="on"></span><span></span></div>
</section>

<section class="services abs">
  <h2 class="section-title abs" style="top:70px">OUR SERVICES</h2>
  <div class="rule abs" style="top:118px"></div>
  <p class="section-sub abs" style="top:138px">Sed ut perspiciatis unde omnis iste natus error sit voluptatem accusantium doloremque laudantium, totam rem aperiam</p>

  <div class="service-card abs" style="left:86px">
    <svg width="80" height="74" viewBox="0 0 80 74"><rect x="4" y="2" width="34" height="72" fill="#222"/><rect x="40" y="20" width="32" height="54" fill="#2a8fd9"/><g fill="#fff"><rect x="10" y="10" width="6" height="6"/><rect x="24" y="10" width="6" height="6"/><rect x="10" y="24" width="6" height="6"/><rect x="24" y="24" width="6" height="6"/><rect x="10" y="38" width="6" height="6"/><rect x="24" y="38" width="6" height="6"/><rect x="46" y="28" width="6" height="5"/><rect x="60" y="28" width="6" height="5"/><rect x="46" y="42" width="6" height="5"/><rect x="60" y="42" width="6" height="5"/><rect x="46" y="56" width="6" height="5"/><rect x="60" y="56" width="6" height="5"/></g></svg>
    <h3>COMMERCIAL</h3>
    <p>Sed ut perspiciatis unde omnis iste natus error sit voluptatem accusantium laudantium totam rem aperiam</p>
  </div>
  <div class="service-card active abs" style="left:346px">
    <svg width="80" height="74" viewBox="0 0 80 74"><path d="M8 36 40 8l32 28" fill="none" stroke="#222" stroke-width="5"/><rect x="54" y="8" width="7" height="16" fill="#222"/><path d="M16 34v36h48V34" fill="none" stroke="#222" stroke-width="5"/><rect x="34" y="46" width="14" height="24" fill="#2a8fd9"/></svg>
    <h3>RESIDENTIAL</h3>
    <p>Sed ut perspiciatis unde omnis iste natus error sit voluptatem accusantium laudantium totam rem aperiam</p>
  </div>
  <div class="service-card abs" style="left:608px">
    <svg width="80" height="74" viewBox="0 0 80 74"><path d="M14 66 62 14" stroke="#2a8fd9" stroke-width="8" stroke-linecap="round"/><path d="M16 12 66 64" stroke="#222" stroke-width="7" stroke-linecap="round"/><circle cx="62" cy="14" r="10" fill="none" stroke="#2a8fd9" stroke-width="5"/></svg>
    <h3>BUILDING MAINTENANCE</h3>
    <p>Sed ut perspiciatis unde omnis iste natus error sit voluptatem accusantium laudantium totam rem aperiam</p>
  </div>
  <div class="service-card abs" style="left:868px">
    <svg width="80" height="74" viewBox="0 0 80 74"><rect x="18" y="14" width="40" height="56" rx="3" fill="none" stroke="#2a8fd9" stroke-width="4"/><rect x="30" y="8" width="16" height="10" fill="#222"/><path d="M26 32h24M26 44h24M26 56h16" stroke="#222" stroke-width="4"/></svg>
    <h3>PROJECT MANAGEMENT</h3>
    <p>Sed ut perspiciatis unde omnis iste natus error sit voluptatem accusantium laudantium totam rem aperiam</p>
  </div>
</section>

<div class="about-img abs" role="img" aria-label="Blue-toned construction site with tower cranes and building frame"></div>
<article class="about-box abs">
  <h2>ABOUT US</h2>
  <div class="rule"></div>
  <p>Sed ut perspiciatis unde omnis iste natus error sit voluptatem accusantium dolore que laudantium, totam rem aperiam, eaque ipsa quae ab illo inventore veritatis et quasi architecto beatae vitae dicta sunt explicabo. Nemo enim ipsam voluptate qu ia voluptas sit aspernatur aut odit aut fugit, sed quia consequuntur magni dolores eos qui ratione voluptatem sequi nesciunt.</p>
  <svg class="corner" width="70" height="54"><polygon points="70,0 70,54 0,54" fill="#1e88d8"/><path d="M40 40h16m-6-6 6 6-6 6" stroke="#fff" stroke-width="3" fill="none"/></svg>
</article>

<section class="testimonials abs" role="img" aria-label="Faint blue city skyline behind the testimonial">
  <h2 class="section-title abs" style="top:100px;color:#fff">OUR TESTIMONIALS</h2>
  <div class="rule abs" style="top:148px;background:#fff"></div>
  <svg class="abs" style="left:120px;top:150px" width="24" height="90"><path d="M20 2 4 45l16 43" stroke="#cde9fb" stroke-width="2" fill="none"/></svg>
  <svg class="abs" style="left:1056px;top:150px" width="24" height="90"><path d="M4 2l16 43L4 88" stroke="#cde9fb" stroke-width="2" fill="none"/></svg>
  <p class="quote abs">Sed ut perspiciatis unde omnis iste natus error sit voluptatem accusantium doloremque laudantium, totam rem aperiam, eaque ipsa quae ab illo inventore veritatis et quasi architecto beatae vitae dicta sunt explicabo. Nemo enim ipsam voluptatem quia voluptas sit aspernatur sed quia consequuntur magni dolores eos qui ratione voluptatem sequi nesciunt.</p>
  <div class="author abs">ALEX CARTER</div>
  <div class="posted abs">Posed on 16 Apr 2018</div>
</section>

<section class="projects abs">
  <h2 class="section-title abs" style="top:26px">OUR PROJECTS</h2>
  <div class="rule abs" style="top:72px"></div>
  <p class="section-sub abs" style="top:94px">Sed ut perspiciatis unde omnis iste natus error sit voluptatem accusantium doloremque laudantium, totam rem aperiam</p>

  <div class="project-card abs" style="left:98px">
    <div class="thumb" role="img" aria-label="Interior building model held over an unfinished room" style="background:linear-gradient(135deg,#e6e6e6,#8a6a55 55%,#c9c9c9)"></div>
    <h3>PROJECTS NAME</h3>
    <p>Sed ut perspiciatis unde omnis iste natus error sit voluptatem accusantium doloremque laudantium, beatae vitae dicta sunt explicabo.</p>
    <span class="btn-more">READ MORE</span>
  </div>
  <div class="project-card active abs" style="left:440px">
    <div class="thumb" role="img" aria-label="Blue wireframe of a glass office building" style="background:linear-gradient(135deg,#d7ecfa,#3c8fd0 60%,#e9f4fc)"></div>
    <h3>PROJECTS NAME</h3>
    <p>Sed ut perspiciatis unde omnis iste natus error sit voluptatem accusantium doloremque laudantium, beatae vitae dicta sunt explicabo.</p>
    <span class="btn-more">READ MORE</span>
  </div>
  <div class="project-card abs" style="left:782px">
    <div class="thumb" role="img" aria-label="Grey city skyline sketch" style="background:linear-gradient(180deg,#e2e2e2,#9a9a9a 60%,#d0d0d0)"></div>
    <h3>PROJECTS NAME</h3>
    <p>Sed ut perspiciatis unde omnis iste natus error sit voluptatem accusantium doloremque laudantium, beatae vitae dicta sunt explicabo.</p>
    <span class="btn-more">READ MORE</span>
  </div>
</section>

<footer class="site-footer abs">
  <div class="footer-brand abs"><span class="dot"></span>KVR Constructions</div>
  <div class="footer-head abs" style="left:488px">QUICK LINKS</div>
  <nav class="footer-links">
    <a style="left:490px;top:74px">Home</a>
    <a style="left:490px;top:102px">About Us</a>
    <a style="left:490px;top:132px">Services</a>
    <a style="left:610px;top:74px">Projects</a>
    <a style="left:610px;top:102px">Culture</a>
    <a style="left:610px;top:132px">News</a>
    <a style="left:610px;top:160px">Contact</a>
  </nav>
  <div class="footer-head abs" style="left:764px">NEWSLETTER</div>
  <p class="news-text abs">Sed ut perspiciatis unde omnis iste natus error sit</p>
  <div class="email abs">Enter Your Email Id :</div>
  <div class="email-btn abs"><svg width="18" height="18" viewBox="0 0 24 24"><path fill="#fff" d="M2 11 22 2l-6 20-4-8-10-3zm10 3 8-10-11 7z"/></svg></div>
  <div class="footer-rule abs"></div>
  <p class="copyright abs">© Copy Right -2018 KVR Constructions.All rights reserved.</p>
</footer>

</body>
</html>
```